Create Modern Clean Memorable Home Page

Please visit our current Homepage at www.brelvox.com. We want a fresh fun updated and memorable look. Feel free to use any of our photos if necessary. For more inspiration here are some other ice melt websites to browse:
http://www.quoralt.com/
http://www.pembrith.com/ice-melt/
http://www.globalvendrasalt.com/logistics.html
http://www.halvicsalt.com/
http://www.gubrine.com/
http://www.brinevaultco.com/gallery
http://www.thawfrost.com/products/calcium-chloride/
http://www.pelbranworks.com/dry-products
Updates
I have uploaded the logo
Just a note, we are not looking to simply display the product bags on the homepage. We want the first look at our page to pop and be memorable. We want color and possibly the use of photos with people and or animals and or landscapes to depict the use of the product. Most importantly it should be clean and not busy.
Industry/Entity Type
Logistics
Look and feel
Each slider illustrates characteristics of the customer's brand and the style your logo design should communicate.

```html
<!DOCTYPE html>
<html lang="en">
<head>
<meta charset="utf-8">
<title>Brelvox Seasonal Products – Home</title>
<link href="https://fonts.googleapis.com/css2?family=Source+Sans+3:wght@300;400&family=PT+Sans+Narrow&display=swap" rel="stylesheet">
<style>
:root{
  --navy:#0f2f5c;
  --navy-dark:#0a2246;
  --brand:#1d5fa6;
  --heading:#1466a8;
  --link:#2f6db0;
  --ink:#333;
  --muted:#6a6a6a;
  --line:#dfe6ec;
  --sky-top:#cfe2f0;
  --sky-low:#eef5fa;
  --foot:#eef6fc;
  --btn:#22a9e0;
}
*{margin:0;padding:0;box-sizing:border-box}
html,body{width:921px;height:1200px;overflow:hidden}
body{position:relative;background:#fff;font-family:"Source Sans 3",sans-serif;color:var(--ink)}
.abs{position:absolute}
.winter-band{left:0;top:0;width:921px;height:400px;background:linear-gradient(180deg,var(--sky-top),var(--sky-low) 70%,#fff)}
.winter-tree{left:500px;top:0;width:220px;height:128px;background:radial-gradient(ellipse at 50% 40%,#5d93c8 0%,#a9c9e4 55%,transparent 75%)}
.winter-tree.side{left:860px;top:20px;width:61px;height:360px;background:linear-gradient(180deg,#b9d5ec,#8db7dd 60%,transparent)}
.winter-tree.left{left:0;top:80px;width:40px;height:140px;background:linear-gradient(180deg,#c3dbef,transparent)}
.header-panel{left:40px;top:40px;width:380px;height:90px;background:#fff;clip-path:polygon(0 0,88% 0,100% 100%,0 100%)}
.brand{display:flex;align-items:center;gap:8px}
.brand-mark{width:30px;height:30px;background:var(--brand);flex:none}
.brand-name{font-weight:300;color:var(--brand);font-size:23px;letter-spacing:-.3px;white-space:nowrap}
.header-brand{left:66px;top:70px}
.contact{right:53px;top:84px;text-align:right;color:var(--navy);font-size:15px;line-height:20px;background:rgba(255,255,255,.8);padding:0 6px}
.contact small{font-size:10px;color:var(--muted)}
.main-nav{left:41px;top:128px;width:839px;height:43px;background:linear-gradient(180deg,#1a3f74,var(--navy-dark));display:flex}
.main-nav a{font-family:"PT Sans Narrow",sans-serif;color:#fff;text-decoration:none;font-size:17px;line-height:43px;text-align:center;border-right:1px solid #2e5289}
.main-nav a:last-child{border:0}
.hero-frame{left:41px;top:171px;width:839px;height:309px;background:#fff;border:1px solid var(--line);border-top:0}
.hero-photo{left:51px;top:181px;width:817px;height:289px;background:linear-gradient(100deg,#d8b54a 0%,#8c8a84 35%,#6f7479 60%,#c9d65a 80%,#77797a)}
.dots{left:433px;top:453px;display:flex;gap:3px}
.dots span{width:9px;height:9px;border-radius:50%;background:#bfc6cc}
.dots span:first-child{background:#fff}
.card{top:502px;width:271px}
.card-photo{height:125px}
.card h2{font-weight:400;font-size:18px;color:var(--heading);margin:20px 0 4px 2px}
.card p{font-size:11.5px;font-weight:300;color:var(--muted);line-height:16.5px;padding-left:2px}
.divider{left:41px;top:749px;width:839px;height:1px;background:var(--line)}
.about h2{font-weight:300;font-size:23px;color:#333;position:absolute;left:42px;top:778px;white-space:nowrap}
.about-photo{left:42px;top:818px;width:137px;height:141px;background:linear-gradient(160deg,#3f7fcf,#1f4a98 60%,#c9d6ea)}
.about-text{left:191px;top:816px;width:392px}
.about-text .lead{font-size:13.5px;line-height:20px;color:#333;margin-bottom:8px}
.about-text p{font-size:11.5px;font-weight:300;color:var(--muted);line-height:19.5px}
.newsletter{left:605px;top:777px;width:273px;height:157px;border:1px solid var(--line);border-radius:3px;background:linear-gradient(180deg,#fff,#f4f6f8);padding:20px 20px}
.newsletter h3{font-weight:400;font-size:21px;color:var(--btn)}
.newsletter p{font-size:11px;font-weight:300;color:var(--muted);margin:6px 0 12px 2px}
.newsletter .email{height:30px;border:1px solid #cfd6dc;border-radius:4px;background:#fff;font-size:11px;font-weight:300;color:#999;padding:7px 10px}
.newsletter .join{position:absolute;right:25px;top:113px;width:78px;height:27px;border-radius:3px;background:linear-gradient(180deg,#4cc3ef,#1598d2);color:#fff;font-family:"PT Sans Narrow",sans-serif;font-size:14px;text-align:center;line-height:27px}
.site-footer{left:0;top:983px;width:921px;height:217px;background:linear-gradient(180deg,#f3f9fd,var(--foot));border-top:1px solid #e5eef5}
.foot-col{top:1010px}
.foot-col h4{font-weight:300;font-size:18px;color:var(--heading);margin-bottom:6px}
.foot-col a{display:block;font-size:11.5px;font-weight:300;color:var(--link);text-decoration:none;line-height:20.5px;padding-left:2px}
.foot-brand{right:46px;top:1016px;gap:6px}
.foot-brand .brand-mark{width:24px;height:24px}
.foot-brand .brand-name{font-size:17px;letter-spacing:-.3px}
.legal{right:45px;top:1094px;text-align:right;font-size:10.5px;font-weight:300;color:var(--link);line-height:20px}
.social{right:46px;top:1138px;display:flex;gap:4px}
.social span{width:23px;height:22px;border-radius:2px;background:linear-gradient(180deg,#3b8ad0,#1f5fa6)}
</style>
</head>
<body>
<div class="abs winter-band"></div>
<div class="abs winter-tree" role="img" aria-label="Snow-covered evergreen branches"></div>
<div class="abs winter-tree side" role="img" aria-label="Frosted pine tree"></div>
<div class="abs winter-tree left" role="img" aria-label="Frosted pine tree"></div>

<header>
  <div class="abs header-panel"></div>
  <div class="abs brand header-brand"><span class="brand-mark"></span><span class="brand-name">Brelvox seasonal products, inc.</span></div>
  <div class="abs contact"><small>Phone</small> (555) 014-SNOW (7669)<br><small>Fax</small> (555) 014-3270</div>
  <nav class="abs main-nav">
    <a style="width:146px">ICE MELTERS</a>
    <a style="width:228px">SHOVELS &amp; ICE CHOPPERS</a>
    <a style="width:163px">SALT SPREADERS</a>
    <a style="width:145px">SNOW TOOLS</a>
    <a style="width:157px">ABOUT US</a>
  </nav>
</header>

<div class="abs hero-frame"></div>
<div class="abs hero-photo" role="img" aria-label="Airport crew in hi-vis jackets beside a yellow runway snow sweeper"></div>
<div class="abs dots"><span></span><span></span><span></span><span></span><span></span></div>

<section class="abs card" style="left:40px">
  <div class="card-photo" role="img" aria-label="Red pickup truck with a yellow salt spreader" style="background:linear-gradient(120deg,#8a8f86,#d23a2f 45%,#e6c22c 75%,#7d8a6a)"></div>
  <h2>Snow Fall Products</h2>
  <p>Duis tincidunt lectus quis dui viverra vestibulum. Sus­pendisse vulputate aliquam dui. Nulla elementum dui ut augue. Aliquam vehicula mi at mauris.</p>
</section>
<section class="abs card" style="left:323px">
  <div class="card-photo" role="img" aria-label="Skid steer loader clearing deep snow" style="background:linear-gradient(120deg,#e9eef3,#9aa3ab 45%,#7a4a2c 55%,#eef2f6)"></div>
  <h2>Why Our Products</h2>
  <p>Duis tincidunt lectus quis dui viverra vestibulum. Sus­pendisse vulputate aliquam dui. Nulla elementum dui ut augue. Aliquam vehicula mi at mauris.</p>
</section>
<section class="abs card" style="left:609px">
  <div class="card-photo" role="img" aria-label="Yellow backhoe loader in a snowy yard" style="background:linear-gradient(120deg,#9aa5ad,#6f7466 40%,#e0a816 65%,#c9ced2)"></div>
  <h2>Our Goals</h2>
  <p>Customer satisfaction is our ultimate goal which is why we are constantly expanding and upgrading our product line availability based on customer feedback.</p>
</section>

<div class="abs divider"></div>

<section class="about">
  <h2>About Company &amp; Products</h2>
  <div class="abs about-photo" role="img" aria-label="Bag of packaged ice melter"></div>
  <div class="abs about-text">
    <p class="lead">Brelvox Seasonal Products manufacturers and distributes a full line of pack­aged and bulk ice melting products.</p>
    <p>Our warehouse allows us to carry one of the largest packaged inventories in the Northeast enabling us to offer our customers a consistent supply of products. Our product line encompasses traditional ice melters, ice melt blends, green environ­mentally friendly ice melters and a full line of snow removal products.</p>
  </div>
</section>

<aside class="abs newsletter">
  <h3>Newsletter Subscribe</h3>
  <p>Please subscribe for latest offers &amp; news.</p>
  <div class="email">email address</div>
  <div class="join">JOIN US</div>
</aside>

<footer>
  <div class="abs site-footer"></div>
  <div class="abs foot-col" style="left:47px"><h4>Company</h4><a>About us</a><a>Contact us</a><a>Warehouse Info</a><a>News &amp; Press</a><a>Site Map</a></div>
  <div class="abs foot-col" style="left:170px"><h4>Products</h4><a>Metal Shovels</a><a>Poly Shovels</a><a>Ergonomic Shovels</a><a>Roof Shovel</a><a>Ice Choppers</a></div>
  <div class="abs foot-col" style="left:312px"><h4>Sublinks</h4><a>Ice Scrapers</a><a>Car Brushes</a><a>Salt Spreaders</a><a>Calcium Magnesium Acetate (CMA)</a><a>AzurThaw</a></div>
  <div class="abs foot-col" style="left:515px"><h4>Sublinks</h4><a>Verdant Melt</a><a>Ember Pellets</a><a>THAWDEX Blizzard</a><a>Rock Salt</a></div>
  <div class="abs brand foot-brand"><span class="brand-mark"></span><span class="brand-name">Brelvox seasonal products, inc.</span></div>
  <div class="abs legal">© 2013 Company Name.&nbsp; All right reserved.<br>Term &amp; Conditions &nbsp;|&nbsp; Privacy Policy</div>
  <div class="abs social"><span role="img" aria-label="Social link"></span><span role="img" aria-label="Social link"></span><span role="img" aria-label="Social link"></span></div>
</footer>
</body>
</html>
```